Verpackungen für Parfum-Proben
Besten Dank! Das Team ist begeistert - also bin ich es auch und wir freuen uns schon, unsere Parfum Proben in Zukunft in diesem tollen Design weitergeben zu können! Danke!
Zielgruppe
Hallo allerseits! Wir sind im Direktvertrieb in den Bereichen Parfum & Kosmetik tätig.
Aufgabenstellung
Für unsere Parfum-Proben benötige ich ein ansprechendes, modernes Design.
Das Design muss relativ neutral gehalten werden, da die Blister sowohl für Herren- als auch Damenproben verwendet werden.
Auf Vorder- und Rückseite soll unser Team-Logo (RuchKontor®) sichtbar sein (Vorderseite größer, Rückseite kleiner).
Auf der linken Innenseite sollte Plätz für einen netten Spruch (den ich mir noch überlege) sein.
Auf der Rückseite muss Platz (weißes / helles Feld) für einen Stempel und/oder Aufkleber (Kontaktdaten des Distributors) sein.
Unser Logo ist Lila - Das farbliche Design sollte dazu passen.
Bei Fragen, einfach Nachricht :)
Daten:
Endformat: 133 x 74 mm
Datenformat: 139 x 80 mm
1-teilig, gestanzt, genutet, einseitig geklebt geliefert
Bitte verwenden Sie für positive Schriftstärken mindestens 9pt (ca. 3,17mm) und bei negativen Schriftstärken mindestens 13pt (ca. 4,59mm).
Abmessungen / Druck- / Designvorlage, Logo, etc.: https://dateiwolke.example/ordner/X7KPtrWQ#m4vbeLhNcyrGzzt9_k2w8p

```html
<!DOCTYPE html>
<html lang="en">
<head>
<meta charset="utf-8">
<title>RuchKontor – Sample Sleeve Layout</title>
<link rel="stylesheet" href="https://fonts.googleapis.com/css2?family=Source+Sans+3:wght@400;500&display=swap">
<style>
  :root {
    --page-bg: #ffffff;
    --navy: #03386a;
    --wave-light: #5c6da6;
    --wave-dark: #3b4a88;
    --strip-light: #7c8ab6;
    --brand-purple: #6c56a6;
    --fold-line: #3b4868;
    --label-white: #ffffff;
    --type-white: #ffffff;
  }
  * { box-sizing: border-box; margin: 0; padding: 0; }
  html, body {
    width: 1200px;
    height: 818px;
    overflow: hidden;
    background: var(--page-bg);
  }
  .canvas {
    position: relative;
    width: 1200px;
    height: 818px;
  }
  .sleeve {
    position: absolute;
    left: 80px;
    top: 123px;
    width: 1040px;
    height: 572px;
    background: var(--navy);
    font-family: "Source Sans 3", "Myriad Pro", sans-serif;
    color: var(--type-white);
    overflow: hidden;
  }
  .sleeve__wave {
    position: absolute;
    inset: 0;
    width: 100%;
    height: 100%;
  }
  .panel {
    position: absolute;
    top: 0;
    width: 520px;
    height: 572px;
  }
  .panel--back { left: 0; }
  .panel--front { left: 520px; border-left: 1px solid var(--fold-line); }
  .brand-name {
    position: absolute;
    left: 0;
    right: 0;
    text-align: center;
    color: var(--brand-purple);
    font-weight: 400;
    letter-spacing: 0.01em;
    line-height: 1;
  }
  .panel--back .brand-name { top: 160px; font-size: 34px; }
  .panel--front .brand-name { top: 150px; font-size: 62px; }
  .tagline {
    position: absolute;
    left: 0;
    right: 0;
    text-align: center;
    font-weight: 400;
    text-transform: uppercase;
    letter-spacing: 0.08em;
  }
  .tagline--sample { top: 340px; font-size: 20px; }
  .tagline--smell { top: 508px; font-size: 31px; letter-spacing: 0.06em; }
  .contact-label {
    position: absolute;
    left: 39px;
    top: 397px;
    width: 426px;
    height: 152px;
    background: var(--label-white);
    border-radius: 8px;
  }
</style>
</head>
<body>
  <main class="canvas">
    <section class="sleeve" aria-label="Perfume sample sleeve, flat layout">
      <svg class="sleeve__wave" viewBox="0 0 1040 572" preserveAspectRatio="none" aria-hidden="true">
        <defs>
          <linearGradient id="wave-fill" x1="0" y1="0" x2="1" y2="0">
            <stop offset="0" stop-color="var(--strip-light)"/>
            <stop offset="0.5" stop-color="var(--wave-light)"/>
            <stop offset="1" stop-color="var(--wave-dark)"/>
          </linearGradient>
        </defs>
        <path d="M0,572 L0,539 C200,530 400,500 520,472 C660,440 720,380 800,355 C880,335 960,336 1040,341 L1040,572 Z" fill="url(#wave-fill)"/>
      </svg>

      <div class="panel panel--back">
        <p class="brand-name">RuchKontor</p>
        <p class="tagline tagline--sample">Free sample for you.</p>
        <div class="contact-label" aria-label="Space for distributor stamp or sticker"></div>
      </div>

      <div class="panel panel--front">
        <p class="brand-name">RuchKontor</p>
        <p class="tagline tagline--smell">Smell well!</p>
      </div>
    </section>
  </main>
</body>
</html>
```